Film Company needs Poster Design Project for upcoming film "CRANE"

At Marrowbend Films, we need a poster design for our upcoming feature film project "CRANE," America first 'rock and roll' star. Our film will cover Silas Wendell Crane's life his drinking, passion and writing. It will not be a horror film, but rather a biopic on his life.
Marrowbend Films is a full service film and television production company, founded by Dale Whitmore and Brevantis, LLC in 2006. Marrowbend Films’ mission is to blend artistic talent with engaging stories to create feature films and television that delight audiences of all ages.
We would like to see designs that embody Silas Wendell Crane as a person. The film will cover most of his famous poems/novels/short stories so any reference to "Hollow clock" or "The Orchard," etc...would work.
Thank you ALL for the amazing work you have submitted, you made it really hard for me to come up with one choice. I will make my decision by Wednesday.
Target audience 18 - 35
It Company

```html
<!DOCTYPE html>
<html lang="en">
<head>
<meta charset="utf-8">
<title>CRANE — Marrowbend Films</title>
<link rel="stylesheet" href="https://fonts.googleapis.com/css2?family=Josefin+Sans:wght@300&family=Arimo:wght@700&display=swap">
<style>
  :root {
    --sand-light: #a8977f;
    --sand-mid: #978670;
    --sand-dark: #7f6f5c;
    --ink: #121212;
    --paper: #ffffff;
    --rust: #922a2a;
  }
  html, body {
    margin: 0;
    padding: 0;
    overflow: hidden;
    background: var(--paper);
  }
  .poster {
    position: relative;
    width: 960px;
    height: 1200px;
    overflow: hidden;
    background: linear-gradient(160deg, var(--sand-light) 0%, var(--sand-mid) 55%, var(--sand-dark) 100%);
  }
  .sand-texture {
    position: absolute;
    inset: 0;
  }
  .title-stem {
    position: absolute;
    left: 53px;
    top: 0;
    width: 47px;
    height: 1200px;
    background: var(--paper);
  }
  .title {
    position: absolute;
    left: 0;
    top: 0;
    width: 960px;
    height: 340px;
  }
  .title text {
    font-family: "Josefin Sans", sans-serif;
    font-weight: 300;
    fill: var(--paper);
  }
  .portrait {
    position: absolute;
    left: 380px;
    top: 373px;
    width: 580px;
    height: 827px;
    background: radial-gradient(ellipse at 45% 40%, #3a3a3a 0%, #1a1a1a 45%, var(--ink) 100%);
    border-radius: 46% 40% 0 0 / 30% 26% 0 0;
  }
  .tagline {
    position: absolute;
    left: 40px;
    top: 420px;
    margin: 0;
    font-family: "Arimo", sans-serif;
    font-weight: 700;
    font-size: 78px;
    line-height: 91px;
    letter-spacing: 1px;
    color: var(--ink);
  }
  .tagline span { display: block; }
  .tagline .accent { color: var(--rust); }
  .bottle-icon {
    position: absolute;
    left: 248px;
    top: 622px;
    width: 110px;
    height: 175px;
  }
  .book-icon {
    position: absolute;
    left: 30px;
    top: 1025px;
    width: 186px;
    height: 136px;
  }
</style>
</head>
<body>
  <main class="poster">
    <div class="sand-texture" role="img" aria-label="Textured sand background in warm beige and brown tones"></div>
    <div class="title-stem"></div>
    <svg class="title" viewBox="0 0 960 340" aria-label="CRANE">
      <text x="48" y="334" font-size="440" textLength="880" lengthAdjust="spacingAndGlyphs">CRANE</text>
    </svg>
    <div class="portrait" role="img" aria-label="Black woven-texture stencil portrait of Silas Wendell Crane"></div>
    <h1 class="tagline">
      <span>AMERICA</span>
      <span>FIRST</span>
      <span class="accent">ROCK</span>
      <span>AND</span>
      <span class="accent">ROLL</span>
      <span>STAR</span>
    </h1>
    <svg class="bottle-icon" viewBox="0 0 110 175" aria-hidden="true">
      <g transform="rotate(20 55 88)" fill="#121212">
        <rect x="44" y="4" width="22" height="14" rx="3"/>
        <path d="M46 18 h18 v26 c0 10 20 18 20 40 v78 c0 6 -4 9 -9 9 h-40 c-5 0 -9 -3 -9 -9 v-78 c0 -22 20 -30 20 -40 z"/>
      </g>
    </svg>
    <svg class="book-icon" viewBox="0 0 186 136" aria-hidden="true">
      <g fill="#121212">
        <path d="M90 22 C70 8 40 4 14 8 V112 C40 108 70 112 90 126 Z"/>
        <path d="M96 22 C116 8 146 4 172 8 V112 C146 108 116 112 96 126 Z"/>
        <path d="M4 24 H10 V118 C40 114 70 118 93 132 C116 118 146 114 176 118 V24 H182 V126 C150 122 120 124 100 136 H86 C66 124 36 122 4 126 Z"/>
      </g>
    </svg>
  </main>
</body>
</html>
```